Fasteners Poly-bag design with VANTRO brand

We are trading with fasteners and rigging hardware and now we need a new design for a poly-bag. The header of poly-bag will contain two parts - top part (around 60%) will be static with our logo "VANTRO" and your type of design. The bottom part (around 40%) should be with different color for each group of fasteners or rigging hardware and with different text (5 groups in total). The border between the two part can be different from straight line (for example like wave or something else). I added a file with explanation and some samples of poly-bags. The total dimensions of the header are 80 mm/40 mm. The nylon part of poly-bag will have a background - I added a file with our image, but you can offer us different image also. Please when creating design, do it for full poly-bag, including the nylon part, not only header. The colors from header can continue to the nylon part also. I added a file "DESIGN SAMPLES" just as examples, what we expect to see. Of course you can offer your own variant of design! Thank you in advance!

Target Market(s)

Fasteners and rigging hardware

Industry/Entity Type

Fastener

Font styles to use
Other font styles liked:
• SAUCER BB - Logo Font

Colors

Designer to choose colors to be used in the design.

Requirements
Must have
• Our logo "VANTRO"

```html
<!DOCTYPE html>
<html lang="en">
<head>
<meta charset="utf-8">
<title>VANTRO poly-bag headers</title>
<link rel="stylesheet" href="https://fonts.googleapis.com/css2?family=Open+Sans:wght@700;800&family=Open+Sans+Condensed:wght@700&display=swap">
<style>
  :root {
    --page: #ffffff;
    --ink: #1b1b1b;
    --white: #ffffff;
    --red-core: #d50a16;
    --red-mid: #a2040e;
    --red-edge: #6c0208;
    --metal-light: #f1f2f3;
    --metal-mid: #c9cbcd;
    --metal-dark: #a9acaf;
    --bag-film: #ebeced;
    --film-red-soft: #f4c9cb;
    --film-red-faint: #f0dcdd;
    --film-green-soft: #c5e6cf;
    --film-green-faint: #dbebdf;
  }
  * { box-sizing: border-box; margin: 0; padding: 0; }
  html, body { width: 1200px; height: 1200px; overflow: hidden; background: var(--page); }
  .sheet { position: relative; width: 1200px; height: 1200px; }

  .bag { position: absolute; top: 144px; width: 459px; height: 918px; }
  .bag--fasteners { left: 108px; }
  .bag--rigging { left: 637px; }

  .header-metal {
    position: absolute; left: 0; top: 0; width: 100%; height: 225px;
    background:
      repeating-linear-gradient(180deg, rgba(255,255,255,0.35) 0 1px, rgba(0,0,0,0.04) 1px 3px, rgba(255,255,255,0.15) 3px 5px),
      linear-gradient(90deg, var(--metal-mid) 0%, var(--metal-light) 30%, var(--metal-dark) 55%, var(--metal-light) 75%, var(--metal-mid) 100%);
  }
  .header-rule { position: absolute; left: 0; top: 225px; width: 100%; height: 4px; background: var(--ink); }

  .hang-slot { position: absolute; left: 165px; top: 22px; width: 122px; height: 40px; }

  .price-badge {
    position: absolute; left: 342px; top: 15px; width: 104px; height: 104px; border-radius: 50%;
    border: 3px solid var(--white);
    background: radial-gradient(circle at 50% 30%, #f0505a 0%, var(--red-core) 45%, #c0040f 100%);
    box-shadow: 0 2px 4px rgba(0,0,0,0.25);
    color: var(--white); text-align: center;
    font-family: "Open Sans Condensed", "Open Sans", sans-serif;
  }
  .price-badge__amount { display: block; margin-top: 22px; font-family: "Open Sans", sans-serif; font-weight: 800; font-size: 24px; line-height: 26px; letter-spacing: 0.5px; }
  .price-badge__note { display: block; margin-top: 3px; font-weight: 700; font-size: 8.5px; line-height: 10px; }

  .brand-name {
    position: absolute; left: 0; top: 112px; width: 100%; text-align: center;
    font-family: "Open Sans", sans-serif; font-weight: 800; font-size: 74px; line-height: 90px;
    color: var(--ink); letter-spacing: 1px;
  }

  .bag-film { position: absolute; left: 0; top: 229px; width: 100%; height: 689px; background-color: var(--bag-film); }
  .bag--fasteners .bag-film {
    background-image:
      radial-gradient(circle at 25% 40%, var(--film-red-soft) 0, transparent 45%),
      radial-gradient(circle at 75% 70%, var(--film-red-soft) 0, transparent 45%),
      linear-gradient(180deg, var(--film-red-faint), var(--bag-film));
  }
  .bag--rigging .bag-film {
    background-image:
      radial-gradient(circle at 25% 40%, var(--film-green-soft) 0, transparent 45%),
      radial-gradient(circle at 75% 70%, var(--film-green-soft) 0, transparent 45%),
      linear-gradient(180deg, var(--film-green-faint), var(--bag-film));
  }

  .group-band { position: absolute; left: 0; top: 229px; width: 459px; height: 148px; }
  .group-name {
    position: absolute; left: 0; top: 251px; width: 100%; text-align: center;
    font-family: "Open Sans", sans-serif; font-weight: 800; font-size: 35px; line-height: 44px;
    color: var(--white);
  }
</style>
</head>
<body>
<main class="sheet">

  <section class="bag bag--fasteners">
    <div class="header-metal"></div>
    <svg class="hang-slot" viewBox="0 0 122 40" aria-hidden="true">
      <path fill="#1b1b1b" d="M14 12 H42 A20 16 0 0 1 80 12 H108 A14 14 0 0 1 108 40 H14 A14 14 0 0 1 14 12 Z"/>
    </svg>
    <div class="price-badge">
      <span class="price-badge__amount">$ 9.99</span>
      <span class="price-badge__note">Department Production<br>Description</span>
    </div>
    <h1 class="brand-name">VANTRO</h1>
    <div class="header-rule"></div>
    <div class="bag-film" role="img" aria-label="Hand-drawn pattern of red screws, bolts, nuts, washers and rivets on light grey film"></div>
    <svg class="group-band" viewBox="0 0 459 148" aria-hidden="true">
      <defs>
        <radialGradient id="bandRedA" cx="0.5" cy="0.45" r="0.6">
          <stop offset="0" stop-color="#d50a16"/>
          <stop offset="0.55" stop-color="#a2040e"/>
          <stop offset="1" stop-color="#6c0208"/>
        </radialGradient>
      </defs>
      <path fill="url(#bandRedA)" d="M0 0 H459 V46 L229.5 146 L0 46 Z"/>
    </svg>
    <p class="group-name">Company Name</p>
  </section>

  <section class="bag bag--rigging">
    <div class="header-metal"></div>
    <svg class="hang-slot" viewBox="0 0 122 40" aria-hidden="true">
      <path fill="#1b1b1b" d="M14 12 H42 A20 16 0 0 1 80 12 H108 A14 14 0 0 1 108 40 H14 A14 14 0 0 1 14 12 Z"/>
    </svg>
    <div class="price-badge">
      <span class="price-badge__amount">$ 9.99</span>
      <span class="price-badge__note">Department Production<br>Description</span>
    </div>
    <h2 class="brand-name">VANTRO</h2>
    <div class="header-rule"></div>
    <div class="bag-film" role="img" aria-label="Hand-drawn pattern of green screws, bolts, nuts, washers and rivets on light grey film"></div>
    <svg class="group-band" viewBox="0 0 459 148" aria-hidden="true">
      <defs>
        <radialGradient id="bandRedB" cx="0.5" cy="0.45" r="0.6">
          <stop offset="0" stop-color="#d50a16"/>
          <stop offset="0.55" stop-color="#a2040e"/>
          <stop offset="1" stop-color="#6c0208"/>
        </radialGradient>
      </defs>
      <path fill="url(#bandRedB)" d="M0 0 H459 V46 L229.5 146 L0 46 Z"/>
    </svg>
    <p class="group-name">Company Name</p>
  </section>

</main>
</body>
</html>
```